Presence Leadership Model

I am looking for a graphic design of the attached leadership model. The colors and design can be altered in any manner that brings the model alive version of the house model.

```html
<!DOCTYPE html>
<html lang="en">
<head>
<meta charset="utf-8">
<title>Presence Leadership Model</title>
<link rel="stylesheet" href="https://fonts.googleapis.com/css2?family=Open+Sans:wght@400;700&display=swap">
<style>
  :root {
    --bronze: #977230;
    --rust: #b35c12;
    --magenta: #ec008c;
    --orange: #d5672d;
    --blue: #3a5c96;
    --green: #359442;
    --white: #ffffff;
  }
  * { margin: 0; padding: 0; box-sizing: border-box; }
  html, body { width: 1200px; height: 1200px; overflow: hidden; background: var(--white); }
  body { font-family: "Open Sans", sans-serif; color: var(--white); }
  .model { position: relative; width: 1200px; height: 1200px; }
  .abs { position: absolute; }

  .presence-band { left: 55px; top: 64px; width: 1094px; height: 260px; background: var(--bronze); border-radius: 40px 40px 0 0; }
  .presence-title {
    left: 383px; top: 31px; width: 442px; height: 68px; background: var(--rust);
    border-radius: 30px; box-shadow: 0 0 0 11px var(--white);
    font-weight: 700; font-size: 38px; line-height: 68px; text-align: center;
  }
  .presence-vision { left: 55px; top: 122px; width: 1094px; text-align: center; font-size: 28px; line-height: 35px; }

  .outer-band {
    left: 55px; top: 222px; width: 1094px; height: 300px; background: var(--magenta);
    border-radius: 45px 45px 0 0; box-shadow: 0 -12px 0 0 var(--white);
  }
  .outer-title { left: 55px; top: 230px; width: 1094px; text-align: center; font-weight: 700; font-size: 29px; line-height: 42px; }

  .level { box-shadow: 0 0 0 13px var(--white); }
  .level-org { left: 55px; top: 337px; width: 380px; height: 596px; background: var(--orange); border-radius: 95px 0 0 95px; }
  .level-personal { left: 780px; top: 337px; width: 372px; height: 596px; background: var(--green); border-radius: 0 95px 95px 0; }
  .level-inter { left: 420px; top: 297px; width: 374px; height: 676px; background: var(--blue); border-radius: 125px; }

  .level-heading { font-weight: 700; font-size: 29px; line-height: 40px; text-align: center; }
  .level-rule { height: 4px; background: var(--white); }
  .method { font-size: 29px; line-height: 40px; text-decoration: underline; text-decoration-thickness: 2px; text-underline-offset: 5px; white-space: nowrap; }

  .steps { list-style: none; font-size: 24.5px; line-height: 36px; letter-spacing: -0.4px; white-space: nowrap; }
  .steps li { position: relative; padding-left: 34px; }
  .steps li::before {
    content: ""; position: absolute; left: 0; top: 9px;
    border-left: 19px solid var(--white); border-top: 10px solid transparent; border-bottom: 10px solid transparent;
  }

  .flow-arrow { overflow: visible; }

  .inner-title {
    left: 55px; top: 989px; width: 1097px; height: 50px; background: var(--magenta); border-radius: 25px;
    font-weight: 700; font-size: 29px; line-height: 50px; text-align: center;
  }
  .inner-group { top: 1048px; height: 115px; background: var(--magenta); }
  .inner-group ul { list-style: none; position: absolute; top: 27px; }
  .inner-group li {
    position: relative; font-weight: 700; font-size: 24.5px; line-height: 38px; white-space: nowrap;
    text-decoration: underline; text-underline-offset: 4px;
  }
  .inner-group li::before {
    content: ""; position: absolute; left: -35px; top: 13px; width: 12px; height: 12px;
    border-radius: 50%; background: var(--white);
  }
</style>
</head>
<body>
<main class="model">
  <div class="abs presence-band"></div>
  <div class="abs presence-title">Presence</div>
  <p class="abs presence-vision">Foster contagious success through<br>people, relationships and a shared vision</p>

  <div class="abs outer-band"></div>
  <h2 class="abs outer-title">Outer (Impact) Strategies</h2>

  <section class="abs level level-org">
    <h3 class="abs level-heading" style="left:0;top:21px;width:364px;">Organization Level</h3>
    <div class="abs level-rule" style="left:44px;top:68px;width:336px;"></div>
    <h4 class="abs method" style="left:89px;top:83px;font-weight:400;">Wins Theory</h4>
    <ul class="abs steps" style="left:54px;top:128px;">
      <li>Develop concrete<br>outcomes, and visible<br>results</li>
      <li>Foster in-depth<br>changes, and new<br>practices</li>
      <li>Have a micro, inter-<br>personal or local<br>impact</li>
      <li>Cultivate positive<br>judgement, and<br>shared ambition</li>
    </ul>
  </section>

  <section class="abs level level-personal">
    <h3 class="abs level-heading" style="left:20px;top:21px;width:332px;">Personal Level</h3>
    <div class="abs level-rule" style="left:27px;top:68px;width:310px;"></div>
    <h4 class="abs method" style="left:99px;top:89px;font-weight:400;">Inner Dialogue</h4>
    <ul class="abs steps" style="left:68px;top:133px;">
      <li>Pause</li>
      <li>Relax</li>
      <li>Open</li>
      <li>Attune to Emergence</li>
      <li>Listen Deeply</li>
      <li>Speak the Truth</li>
    </ul>
  </section>

  <section class="abs level level-inter">
    <h3 class="abs level-heading" style="left:0;top:37px;width:374px;">Interpersonal Level</h3>
    <div class="abs level-rule" style="left:25px;top:89px;width:313px;"></div>
    <h4 class="abs method" style="left:0;top:123px;width:374px;text-align:center;font-weight:400;">Heart Listening</h4>
    <ul class="abs steps" style="left:47px;top:168px;">
      <li>Ask open-ended<br>questions</li>
      <li>Affirm someone’s<br>strengths, efforts and<br>past success</li>
      <li>Reflect back what is<br>shared for confirma-<br>tion</li>
      <li>Summarize key points<br>to gain insights</li>
      <li>Share and develop<br>mutual expertise</li>
    </ul>
  </section>

  <svg class="abs flow-arrow" style="left:350px;top:694px;" width="96" height="76" viewBox="0 0 96 76" aria-hidden="true">
    <polygon points="2,38 52,2 48,26 94,15 72,40 92,60 46,52 52,74" fill="var(--magenta)" stroke="var(--white)" stroke-width="5" stroke-linejoin="miter"/>
  </svg>
  <svg class="abs flow-arrow" style="left:750px;top:700px;" width="96" height="66" viewBox="0 0 96 66" aria-hidden="true">
    <polygon points="2,32 47,2 44,22 92,10 74,34 92,54 44,44 47,64" fill="var(--magenta)" stroke="var(--white)" stroke-width="5" stroke-linejoin="miter"/>
  </svg>

  <h2 class="abs inner-title">Inner (Wellbeing) Strategies</h2>

  <section class="abs inner-group" style="left:52px;width:369px;">
    <ul style="left:70px;"><li>Physical Fitness</li><li>Nutrition</li></ul>
  </section>
  <section class="abs inner-group" style="left:431px;width:357px;">
    <ul style="left:56px;"><li>Heart Rate Variability</li><li>Neurofeedback</li></ul>
  </section>
  <section class="abs inner-group" style="left:797px;width:355px;border-radius:0 0 12px 0;">
    <ul style="left:60px;"><li>Coastal Ramble Club</li><li>Video Gaming Club</li></ul>
  </section>
</main>
</body>
</html>
```